Executive & Leadership Coach needs a Graphic Design

We need a graphic design for a Leadership methodology/strategy that can be linked to The Harbor Prism

The Harbor Prism consists of:
1. Achievements
2. Personal Brand
3. Network
4. Executive Presence

This should Graphic Design will need to be used in PowerPoint presentations, training manuals and web pages

The design should be modern and provide the feeling of strength, trust, energy & creativity

Industry/Entity Type

Graphic Design

Other font styles liked:
• Calibri, Verdana

```html
<!DOCTYPE html>
<html lang="en">
<head>
<meta charset="utf-8">
<title>The Harbor Prism – Leadership Model</title>
<link rel="stylesheet" href="https://fonts.googleapis.com/css2?family=Open+Sans:wght@400;700&display=swap">
<style>
  :root {
    --canvas-bg: #ffffff;
    --ink: #333333;
    --gear-blue: #29abe2;
    --gear-green: #8dc63f;
    --gear-orange: #f7941d;
    --gear-purple: #662d91;
    --gear-pink: #ed1e79;
    --hub: #ffffff;
    --hub-edge: rgba(0, 0, 0, 0.14);
  }
  html, body {
    margin: 0;
    padding: 0;
    overflow: hidden;
  }
  .canvas {
    position: relative;
    width: 1200px;
    height: 1000px;
    background: var(--canvas-bg);
    overflow: hidden;
    font-family: "Open Sans", Verdana, sans-serif;
    color: var(--ink);
  }
  .gear-field {
    position: absolute;
    inset: 0;
  }
  .gear {
    filter: drop-shadow(2px 3px 3px rgba(0, 0, 0, 0.35));
  }
  .gear--achievements { color: var(--gear-blue); }
  .gear--presence { color: var(--gear-green); }
  .gear--core { color: var(--gear-orange); }
  .gear--network { color: var(--gear-purple); }
  .gear--brand { color: var(--gear-pink); }
  .gear-body { fill: currentColor; }
  .gear-hub {
    fill: var(--hub);
    stroke: var(--hub-edge);
    stroke-width: 2;
  }
  .label {
    position: absolute;
    display: flex;
    align-items: center;
    justify-content: center;
    text-align: center;
    transform: translate(-50%, -50%);
    width: 170px;
    height: 120px;
    line-height: 1.2;
    margin: 0;
    font-weight: 400;
  }
  .label--achievements { left: 377px; top: 337px; font-size: 21px; }
  .label--presence { left: 850px; top: 337px; font-size: 24px; }
  .label--network { left: 447px; top: 677px; font-size: 24px; }
  .label--brand { left: 797px; top: 677px; font-size: 24px; }
  .label--core {
    left: 620px;
    top: 472px;
    width: 200px;
    font-size: 35px;
    font-weight: 700;
    line-height: 1.15;
  }
</style>
</head>
<body>
<main class="canvas">
  <svg class="gear-field" width="1200" height="1000" viewBox="0 0 1200 1000" aria-hidden="true">
    <defs>
      <polygon id="tooth-small" class="gear-body" points="-18,-96 -14,-128 14,-128 18,-96"/>
      <polygon id="tooth-large" class="gear-body" points="-21,-120 -16,-160 16,-160 21,-120"/>
      <symbol id="gear-small" viewBox="-130 -130 260 260" overflow="visible">
        <circle class="gear-body" r="102"/>
        <use href="#tooth-small"/>
        <use href="#tooth-small" transform="rotate(36)"/>
        <use href="#tooth-small" transform="rotate(72)"/>
        <use href="#tooth-small" transform="rotate(108)"/>
        <use href="#tooth-small" transform="rotate(144)"/>
        <use href="#tooth-small" transform="rotate(180)"/>
        <use href="#tooth-small" transform="rotate(216)"/>
        <use href="#tooth-small" transform="rotate(252)"/>
        <use href="#tooth-small" transform="rotate(288)"/>
        <use href="#tooth-small" transform="rotate(324)"/>
        <circle class="gear-hub" r="81"/>
      </symbol>
      <symbol id="gear-large" viewBox="-165 -165 330 330" overflow="visible">
        <circle class="gear-body" r="128"/>
        <use href="#tooth-large"/>
        <use href="#tooth-large" transform="rotate(30)"/>
        <use href="#tooth-large" transform="rotate(60)"/>
        <use href="#tooth-large" transform="rotate(90)"/>
        <use href="#tooth-large" transform="rotate(120)"/>
        <use href="#tooth-large" transform="rotate(150)"/>
        <use href="#tooth-large" transform="rotate(180)"/>
        <use href="#tooth-large" transform="rotate(210)"/>
        <use href="#tooth-large" transform="rotate(240)"/>
        <use href="#tooth-large" transform="rotate(270)"/>
        <use href="#tooth-large" transform="rotate(300)"/>
        <use href="#tooth-large" transform="rotate(330)"/>
        <circle class="gear-hub" r="104"/>
      </symbol>
    </defs>

    <use class="gear gear--network" href="#gear-small" x="317" y="547" width="260" height="260" transform="rotate(8 447 677)"/>
    <use class="gear gear--brand" href="#gear-small" x="667" y="547" width="260" height="260" transform="rotate(4 797 677)"/>
    <use class="gear gear--achievements" href="#gear-small" x="247" y="207" width="260" height="260" transform="rotate(2 377 337)"/>
    <use class="gear gear--presence" href="#gear-small" x="720" y="207" width="260" height="260" transform="rotate(0 850 337)"/>
    <use class="gear gear--core" href="#gear-large" x="455" y="307" width="330" height="330"/>
  </svg>

  <p class="label label--achievements">Achievements</p>
  <p class="label label--presence">Executive<br>Presence</p>
  <p class="label label--network">Network</p>
  <p class="label label--brand">Personal<br>Brand</p>
  <h1 class="label label--core">Harbor<br>Prism</h1>
</main>
</body>
</html>
```